TELVA EV

We need a business card design for a new Luxury golf cart Company Telva. We manufacture and sell high end golf carts. We would like to see designs that are high end. I have the logo so really need a nice clean look.

```html
<!DOCTYPE html>
<html lang="en">
<head>
<meta charset="utf-8">
<title>Telva EV – Business Card</title>
<link href="https://fonts.googleapis.com/css2?family=Montserrat:wght@300;400;700;800&display=swap" rel="stylesheet">
<style>
  :root {
    --backdrop: #d1d5d5;
    --card-white: #fdfdfe;
    --brand-green: #073a2f;
    --name-green: #0c3a30;
    --text-grey: #4b4d4f;
    --edge-blue: #1a8fb6;
  }
  * { margin: 0; padding: 0; box-sizing: border-box; }
  html, body {
    width: 1200px; height: 1200px; overflow: hidden;
    background: var(--backdrop);
    font-family: "Montserrat", sans-serif;
  }
  .sheet {
    width: 1200px; height: 1200px;
    display: flex; flex-direction: column; align-items: center; justify-content: center;
    gap: 56px;
  }
  .card {
    width: 900px; height: 514px; position: relative;
    border-bottom: 4px solid var(--edge-blue);
    box-shadow: 0 18px 40px rgba(0,0,0,0.18);
  }
  .card-front { background: var(--card-white); }
  .card-back {
    background: var(--brand-green);
    display: flex; align-items: center; justify-content: center;
  }
  .person { position: absolute; left: 78px; top: 70px; }
  .person-name {
    font-weight: 700; font-size: 38px; color: var(--name-green); letter-spacing: 0.3px;
  }
  .person-title {
    font-weight: 300; font-size: 24px; color: var(--text-grey); margin-top: 4px;
  }
  .address {
    position: absolute; left: 78px; top: 212px;
    font-size: 22px; font-weight: 400; color: var(--text-grey); line-height: 1.35;
  }
  .contacts {
    position: absolute; left: 48px; top: 292px; list-style: none;
    font-size: 22px; color: var(--text-grey); line-height: 1.35;
  }
  .contacts li { display: flex; align-items: center; gap: 10px; }
  .contacts svg { width: 20px; height: 20px; fill: var(--name-green); flex: none; }
  .front-wordmark {
    position: absolute; right: 70px; bottom: 64px;
    font-weight: 800; font-size: 62px; letter-spacing: 4px; color: var(--brand-green);
  }
  .back-wordmark {
    font-weight: 800; font-size: 150px; letter-spacing: 10px; color: #ffffff;
  }
</style>
</head>
<body>
<main class="sheet">
  <section class="card card-front">
    <div class="person">
      <h1 class="person-name">Marlow Pierce</h1>
      <p class="person-title">Founder &amp; Director</p>
    </div>
    <address class="address" style="font-style:normal">
      1180 Harbor Reed Ave #12<br>
      Seabrook, SC 29455
    </address>
    <ul class="contacts">
      <li>
        <svg viewBox="0 0 24 24" aria-hidden="true"><path d="M6.6 10.8a15.1 15.1 0 0 0 6.6 6.6l2.2-2.2a1 1 0 0 1 1-.25 11.4 11.4 0 0 0 3.6.57 1 1 0 0 1 1 1V20a1 1 0 0 1-1 1A17 17 0 0 1 3 4a1 1 0 0 1 1-1h3.5a1 1 0 0 1 1 1c0 1.25.2 2.45.57 3.57a1 1 0 0 1-.25 1z"/></svg>
        843-555-0142
      </li>
      <li>
        <svg viewBox="0 0 24 24" aria-hidden="true"><path d="M2 5h20v14H2z M3.5 6.5 12 13l8.5-6.5" fill="none" stroke="var(--name-green)" stroke-width="2"/><path d="M2 5h20L12 12z"/></svg>
        info@telva-ev.com
      </li>
      <li>
        <svg viewBox="0 0 24 24" aria-hidden="true"><circle cx="12" cy="12" r="9" fill="none" stroke="var(--name-green)" stroke-width="2"/><path d="M3 12h18M12 3c3 3 3 15 0 18M12 3c-3 3-3 15 0 18" fill="none" stroke="var(--name-green)" stroke-width="1.6"/></svg>
        www.telva-ev.com
      </li>
    </ul>
    <div class="front-wordmark">TELVA</div>
  </section>

  <section class="card card-back">
    <div class="back-wordmark">TELVA</div>
  </section>
</main>
</body>
</html>
```